Business Brochure / White Paper

This white paper is a marketing document to showcase ourselves to other businesses (private hospitals and other premium healthcare providers). The document should consist of bold and beautiful graphics. As an example of the sort of thing that we mean, we have attached the "velmora sky lineage records" white paper. It should consist of several A4 pages.
The content for the white paper is attached. Note that the content document is only a scaffold for the white paper and the exact layout does not need to be followed (especially text boxes which have just been placed roughly). You are free to use your artistic license to move content around in order to make the document as catchy as possible.
We have also included graphics that we have purchased licenses to and that we encourage to be used as you see fit. Note that in some places we have added a note after two asterisks (i.e. **) when we would like you to add specific images/graphics.
All of the relevant documents and graphics/images to be used to make the white paper can be found at the below link:
https://www.filquarry.net/sh/zhtwmekbb41paxl/BBDN5K3TB8FWLPNTq1tGmeOWRc?dl=0
Feel free to ask any questions.
Good Luck!
Hi,
Thank you for your submissions so far.
Please use our dropbox link for an updated and much more specific brief on what we require in terms of content, layout, and components:
Please note that we must make a decision within 3 days' time.
Please also note that we cannot select a designer unless designs for ALL PAGES of the white paper are submitted.
Thank you and good luck!

```html
<!DOCTYPE html>
<html lang="en">
<head>
<meta charset="utf-8">
<title>Vireogen – Business Partner, pages 2–3</title>
<link href="https://fonts.googleapis.com/css2?family=Roboto:wght@400;500;700&family=EB+Garamond:ital,wght@1,400;1,600&display=swap" rel="stylesheet">
<style>
  :root{
    --backdrop:#cbdbe9;
    --paper:#ffffff;
    --brand-blue:#1467ad;
    --deep-blue:#0a62b3;
    --teal:#1a8f8a;
    --lime:#8dc043;
    --ink:#2e3338;
    --muted:#8a8f94;
    --caption:#1d6aa8;
  }
  *{margin:0;padding:0;box-sizing:border-box}
  html,body{width:1200px;height:979px;overflow:hidden;background:var(--backdrop)}
  body{position:relative;font-family:"Roboto",Arial,sans-serif;color:var(--ink)}
  .spread{position:absolute;left:110px;top:96px;width:980px;height:688px;background:var(--paper)}
  .abs{position:absolute}
  .running-head{font-size:6.4px;letter-spacing:2.2px;color:var(--muted);font-weight:500;top:28px}
  .folio{font-size:6.4px;color:var(--muted);top:28px}
  .title-bar{height:12px;width:57px;background:var(--brand-blue);top:58px}
  .page-title{font-size:16px;font-weight:500;top:55px;letter-spacing:.1px;color:var(--ink)}
  .photo-lab{left:57px;top:117px;width:249px;height:201px;
    background:radial-gradient(circle at 40% 55%,#b7cfe0 0,#9bbcd6 40%,#c9dbe8 100%)}
  .fact-box{left:306px;top:117px;width:183px;height:201px;
    background:linear-gradient(160deg,#0b5eb6 0%,#0d66b0 60%,#168a8f 100%);color:#fff;padding:53px 20px 0 20px}
  .fact-box h3{font-size:12px;font-weight:500;margin-bottom:10px;letter-spacing:.2px}
  .fact-box p{font-size:9.6px;line-height:12px}
  .quote-mark{left:406px;top:108px}
  .section-head{left:56px;top:358px;font-size:11.5px;font-weight:500;color:var(--ink)}
  .body-text{font-size:7.3px;line-height:10.4px;color:var(--ink)}
  .justify{text-align:justify}
  .intro{left:56px;top:391px;width:392px}
  .col-a{left:56px;top:463px;width:193px}
  .col-b{left:260px;top:463px;width:193px}
  .accent-square{left:0;top:598px;width:57px;height:57px;background:var(--lime)}
  .pull-quote{left:80px;top:600px;width:373px;font-family:"EB Garamond",Georgia,serif;font-style:italic;font-size:7.2px;line-height:9.6px}
  .attribution{left:240px;top:643px;width:213px;text-align:right;font-family:"EB Garamond",Georgia,serif;font-size:5.6px;line-height:7px}
  .attribution b{font-weight:600}
  .photo-helix{left:489px;top:117px;width:491px;height:301px;
    background:linear-gradient(120deg,#0b58b8 0%,#1b7fd0 35%,#3ea6d9 55%,#1e9a8e 80%,#7cc07a 100%)}
  .promo-box{left:546px;top:373px;width:142px;height:129px;background:var(--lime);color:#fff;
    padding:27px 14px 0 17px;font-size:10.4px;font-weight:700;line-height:12.4px}
  .side-copy{left:719px;top:446px;width:219px}
  .partner-copy{left:546px;top:530px;width:392px}
  .page-caption{position:absolute;left:0;width:1200px;top:866px;text-align:center;font-size:21px;letter-spacing:3.5px;color:var(--caption)}
</style>
</head>
<body>
  <main class="spread">
    <!-- left page -->
    <div class="abs running-head" style="left:57px">VIREOGEN - BUSINESS PARTNER</div>
    <div class="abs folio" style="left:430px">2</div>
    <div class="abs title-bar" style="left:0"></div>
    <h1 class="abs page-title" style="left:89px">ABOUT US</h1>

    <div class="abs photo-lab" role="img" aria-label="Photo of a scientist in glasses holding a clear capsule with a DNA helix inside"></div>
    <aside class="abs fact-box">
      <h3>DID YOU KNOW?</h3>
      <p>Response rates for many prescribed drugs are as low as 50% and that genetic factors can account for up to 95% of drug-response variability and susceptibility!<sup style="font-size:5px">1,2,3</sup> That’s why physicians are turning to precision prescribing!</p>
    </aside>
    <svg class="abs quote-mark" width="44" height="30" viewBox="0 0 44 30" aria-hidden="true">
      <path fill="#8dc043" d="M0 0h18v16c0 8-4 13-12 14l-1-5c4-1 6-3 6-7H0z M26 0h18v16c0 8-4 13-12 14l-1-5c4-1 6-3 6-7H26z"/>
    </svg>

    <h2 class="abs section-head">PRECISION MEDICINE</h2>
    <p class="abs body-text intro">The Harlow Ridge Clinic, Ashbury Vale Hospital, Lakemont Clinic and Northgate General Hospital. These are just some of the world’s most reputable medical clinics that are already offering genomic and precision healthcare to their patients. Premium healthcare providers around the world, including private hospitals, high-end primary care practices, executive health providers and concierge medicine clinics, are rapidly following suit.</p>
    <p class="abs body-text justify col-a">Ever since the human genome was decoded, a plethora of scientific research has been compiled and the amount of new research and actionable data has grown at an exponential rate. The science has been moving much faster than industry can keep up with but precision medicine is now quickly becoming mainstream practise. The revolution has begun and genomic-driven precision medicine is set to become the new standard in healthcare delivery.</p>
    <p class="abs body-text justify col-b"><b>Vireogen™</b> partners with premium health providers like you to take your business to the next level and set you apart from competitors. Our cutting-edge products allow you to offer the same in world-class precision and genomic healthcare. The science is clear, the technology is ready, and the time for clinical implementation is now.</p>

    <div class="abs accent-square"></div>
    <blockquote class="abs pull-quote">“Doctors have always recognized that every patient is unique, and doctors have always tried to tailor their treatments as best they can to individuals. You can match a blood transfusion to a blood type — that was an important discovery. What if matching a cancer cure to our genetic code was just as easy, just as standard? What if figuring out the right dose of medicine was as simple as taking our temperature?”</blockquote>
    <p class="abs attribution"><b>— Senator Adela Marwick,</b> at the announcement of a $215 Million<br>Precision-Medicine Genetic Plan, January 30, 2015.<sup>4</sup></p>

    <!-- right page -->
    <div class="abs running-head" style="left:546px">VIREOGEN - BUSINESS PARTNER</div>
    <div class="abs folio" style="left:920px">3</div>
    <div class="abs title-bar" style="left:489px"></div>
    <h1 class="abs page-title" style="left:578px">LUCRATIVE NEW REVENUE STREAM</h1>

    <div class="abs photo-helix" role="img" aria-label="Illustration of a glowing DNA double helix over a blue-green data grid with a businessman silhouette"></div>
    <div class="abs promo-box">Effortlessly increase your businesses’ revenues by hundreds to thousands of US dollars per patient per year.</div>
    <p class="abs body-text side-copy">Genomic and precision medicine applications open a whole world of lucrative new revenue streams. Increase your businesses’ revenue by hundreds to thousands of United States dollars per patient per year. Upsell to existing patients and attract new customers by offering the latest in world-class technology.</p>
    <p class="abs body-text partner-copy"><b>Vireogen™</b> strategically partners with appropriate and reputable healthcare providers to enable their patients access to genomic and precision medicine services. Our partners do not invest any capital so there is no risk. Partners simply stock and sell Vireogen products so we only profit when they do. Patients have a variety of products on offer with varying value and corresponding price points. Vireogen remains committed to ensuring that our products remain affordably accessible to the self-pay patient market and expect the same from partners.</p>
  </main>
  <div class="page-caption">page 2-3</div>
</body>
</html>
```